New Business Card Design Project

Use the flyer uploaded and website www.brightoakbuilders.example for inspiration.
List Our Services on Backside of business cards
Marcus Dell
Harborline Renovations Inc.
Licensed General Contractors
555-014-7390

Contact Information for Business Card

Use the flyer uploaded and website www.brightoakbuilders.example for inspiration. List Our Services on Backside of business cards Marcus Dell Harborline Renovations Inc. Licensed General Contractors 555-014-7390

```html
<!DOCTYPE html>
<html lang="en">
<head>
<meta charset="utf-8">
<title>Harborline Renovations – Business Cards</title>
<link href="https://fonts.googleapis.com/css2?family=Montserrat:wght@300;400;500;600;800&display=swap" rel="stylesheet">
<style>
  :root{
    --stage:#d6d9dc;
    --card:#1b1b1b;
    --ink:#f2f2f2;
    --muted:#cfcfcf;
    --band:#ffffff;
    --dark-text:#111111;
  }
  html,body{margin:0;padding:0;overflow:hidden;}
  body{
    width:1200px;height:900px;background:var(--stage);
    font-family:'Montserrat',sans-serif;position:relative;
  }
  .card{
    position:absolute;left:250px;width:700px;height:400px;
    background:var(--card);color:var(--ink);overflow:hidden;
    box-shadow:0 6px 18px rgba(0,0,0,.25);
  }
  .card--back{top:30px;}
  .card--front{top:470px;}

  .brand-name{
    font-weight:300;text-transform:uppercase;letter-spacing:3px;
    color:var(--ink);margin:0;white-space:nowrap;
  }

  /* back side */
  .card--back .brand-name{
    position:absolute;top:80px;left:0;right:0;text-align:center;font-size:30px;
  }
  .services-title{
    position:absolute;top:165px;left:0;right:0;text-align:center;
    font-size:19px;font-weight:600;margin:0;
  }
  .services-title span{display:inline-block;padding-bottom:6px;border-bottom:1px solid var(--muted);}
  .services-list{
    position:absolute;top:230px;left:30px;right:30px;margin:0;padding:0;list-style:none;
    text-align:center;font-size:13.5px;font-weight:400;line-height:2.1;color:var(--muted);
  }
  .services-list li{display:inline;margin:0 6px;}
  .services-list li::before{content:"•";margin-right:5px;}

  /* front side */
  .card--front .brand-name{
    position:absolute;top:120px;left:70px;font-size:26px;
  }
  .band{position:absolute;left:0;top:0;width:700px;height:400px;}
  .person{position:absolute;left:40px;top:272px;color:var(--dark-text);}
  .person-name{margin:0;font-size:27px;font-weight:800;line-height:1;}
  .person-role{margin:4px 0 0;font-size:14px;font-weight:500;}
  .contact{position:absolute;display:flex;align-items:center;gap:10px;font-size:15px;}
  .contact svg{width:16px;height:16px;}
  .contact--phone{right:40px;top:225px;}
  .contact--web{left:40px;top:352px;}
  .license{position:absolute;right:40px;top:290px;font-size:15px;color:var(--dark-text);}
</style>
</head>
<body>

<section class="card card--back" aria-label="Card back: services">
  <h2 class="brand-name">Harborline Renovations</h2>
  <h3 class="services-title"><span>Our Services</span></h3>
  <ul class="services-list">
    <li>Remodel: Kitchen &amp; Bath</li>
    <li>Painting: Interior &amp; Exterior</li>
    <li>Flooring: Carpet, Vinyl, Wood</li>
    <li>Window: Door Replacement</li>
    <li>Plumbing: Repair &amp; Upgrades</li>
    <li>Energy Efficient Upgrades</li>
    <li>Deck &amp; Patio construction</li>
    <li>Water &amp; Mold Damage</li>
    <li>Garage Renovation</li>
  </ul>
</section>

<section class="card card--front" aria-label="Card front: contact">
  <svg class="band" viewBox="0 0 700 400" aria-hidden="true">
    <polygon points="0,265 320,265 370,332 0,332" fill="var(--band)"/>
    <polygon points="348,265 700,265 700,332 398,332" fill="var(--band)"/>
  </svg>

  <h2 class="brand-name">Harborline Renovations</h2>

  <div class="contact contact--phone">
    <svg viewBox="0 0 24 24" aria-hidden="true"><path fill="var(--ink)" d="M6.6 10.8a15.2 15.2 0 0 0 6.6 6.6l2.2-2.2a1 1 0 0 1 1-.25 11.4 11.4 0 0 0 3.6.57 1 1 0 0 1 1 1V20a1 1 0 0 1-1 1A17 17 0 0 1 3 4a1 1 0 0 1 1-1h3.5a1 1 0 0 1 1 1c0 1.25.2 2.45.57 3.57a1 1 0 0 1-.25 1z"/></svg>
    <span>555-014-7390</span>
  </div>

  <div class="person">
    <p class="person-name">Marcus Dell</p>
    <p class="person-role">Managing Director</p>
  </div>

  <p class="license">CSLB Licensed No. #4820156</p>

  <div class="contact contact--web">
    <svg viewBox="0 0 24 24" aria-hidden="true"><circle cx="12" cy="12" r="9" fill="none" stroke="var(--ink)" stroke-width="2"/><path d="M3 12h18M12 3c3 3 3 15 0 18M12 3c-3 3-3 15 0 18" fill="none" stroke="var(--ink)" stroke-width="1.5"/></svg>
    <span>www.brightoakbuilders.example</span>
  </div>
</section>

</body>
</html>
```